Marlow Crest Group (Real Estate and Investment)

A high end, clean design.
We are a real estate company with sales, asset management and investment divisions. We want to use a black and white scheme which is really high end feel. The back of the card can just be the logo (black background with the white writing) as we will probably emboss this when we print)

Target Market(s)

High level investors, high end houses for sale

Industry/Entity Type

Business

Contact Information for Business Card

Name, position, phone number and email address
Glen Varley, Managing Director, 0437259064 and glen@marlowcrest-example.com.au

Requirements
Must have
• Back of the card to be the black background with the white writing (as per the attached images). Would like the capacity to emboss the writing and logo

```html
<!DOCTYPE html>
<html lang="en">
<head>
<meta charset="utf-8">
<title>Marlow Crest Group – Business Card</title>
<link rel="stylesheet" href="https://fonts.googleapis.com/css2?family=Roboto:wght@400;500&family=Questrial&display=swap">
<style>
  :root {
    --canvas: #ffffff;
    --card-dark: #232226;
    --card-dark-deep: #1e1b22;
    --card-glow: #2e2a33;
    --panel-light: #ebebeb;
    --ink: #1c1c1c;
    --white: #ffffff;
    --accent-orange: #e8862a;
    --accent-green: #8cc152;
    --accent-blue: #2f9fd8;
  }
  * { box-sizing: border-box; margin: 0; padding: 0; }
  html, body { width: 1200px; height: 1200px; overflow: hidden; background: var(--canvas); }
  .canvas { position: relative; width: 1200px; height: 1200px; }

  .dark-surface {
    background:
      radial-gradient(ellipse at 50% 45%, #251d2b 0%, var(--card-dark-deep) 45%, transparent 75%),
      linear-gradient(135deg, var(--card-dark) 0%, var(--card-glow) 50%, var(--card-dark) 100%);
  }

  .brand-mark { display: flex; flex-direction: column; align-items: center; color: var(--white); }
  .brand-mark__circle { border: 2px solid var(--white); border-radius: 50%; }
  .brand-mark__name {
    font-family: "Roboto", sans-serif; font-weight: 400;
    text-transform: uppercase; letter-spacing: -0.5px; white-space: nowrap; line-height: 1;
  }

  /* Front card */
  .card-front { position: absolute; left: 149px; top: 41px; width: 905px; height: 541px; }
  .card-front__brand {
    position: absolute; left: 0; top: 0; width: 452px; height: 541px;
    justify-content: center; padding-bottom: 30px;
  }
  .card-front__brand .brand-mark__circle { width: 178px; height: 178px; margin-bottom: 52px; }
  .card-front__brand .brand-mark__name { font-size: 36px; }

  .card-front__name-panel {
    position: absolute; left: 453px; top: 0; width: 452px; height: 253px;
    background: var(--panel-light); display: flex; align-items: center; justify-content: center;
  }
  .card-front__name {
    font-family: "Roboto", sans-serif; font-weight: 500; font-size: 64px;
    color: var(--ink); letter-spacing: 0.5px;
  }

  .accent-rail { position: absolute; left: 453px; top: 253px; width: 6px; height: 288px; display: flex; flex-direction: column; }
  .accent-rail span { flex: 1; }
  .accent-rail .orange { background: var(--accent-orange); }
  .accent-rail .green { background: var(--accent-green); }
  .accent-rail .blue { background: var(--accent-blue); }

  .contact-list { position: absolute; left: 469px; top: 253px; width: 436px; list-style: none; }
  .contact-item {
    position: absolute; left: 0; display: flex; align-items: center; gap: 18px;
    font-family: "Questrial", sans-serif; color: var(--ink); white-space: nowrap;
  }
  .contact-item--phone { top: 54px; font-size: 34px; }
  .contact-item--email { top: 134px; font-size: 25px; }
  .contact-item--address { top: 216px; font-size: 31px; }
  .contact-item--address .contact-item__text { margin-left: 18px; }
  .contact-icon {
    width: 46px; height: 46px; border-radius: 50%; background: var(--ink);
    display: flex; align-items: center; justify-content: center; flex-shrink: 0;
  }

  /* Back card */
  .card-back { position: absolute; left: 144px; top: 610px; width: 904px; height: 542px; }
  .card-back__brand { position: absolute; left: 0; top: 0; width: 904px; padding-top: 134px; }
  .card-back__brand .brand-mark__circle { width: 180px; height: 180px; margin-bottom: 44px; }
  .card-back__brand .brand-mark__name { font-size: 48px; }

  .accent-band { position: absolute; left: 0; top: 406px; width: 904px; height: 6px; display: flex; }
  .accent-band span { flex: 1; }
  .accent-band .blue { background: var(--accent-blue); }
  .accent-band .green { background: var(--accent-green); }
  .accent-band .orange { background: var(--accent-orange); }

  .card-back__details {
    position: absolute; left: 0; top: 436px; width: 904px; text-align: center;
    font-family: "Questrial", sans-serif; font-size: 31px; line-height: 41px; color: var(--white);
  }
</style>
</head>
<body>
<main class="canvas">

  <section class="card-front" aria-label="Business card front">
    <div class="card-front__brand brand-mark dark-surface">
      <div class="brand-mark__circle"></div>
      <div class="brand-mark__name">Marlow Crest Group</div>
    </div>

    <div class="card-front__name-panel">
      <h1 class="card-front__name">Glen Varley</h1>
    </div>

    <div class="accent-rail"><span class="orange"></span><span class="green"></span><span class="blue"></span></div>

    <ul class="contact-list">
      <li class="contact-item contact-item--phone">
        <span class="contact-icon">
          <svg width="24" height="24" viewBox="0 0 24 24" aria-hidden="true">
            <path d="M6 3c1 0 2 3 2 4s-1.5 1.5-1.5 2.5c0 2 4 6.5 6 6.5 1 0 1.5-1.5 2.5-1.5s4 1 4 2-2 4-4 4C9 20.5 3.5 15 3.5 8c0-2 1.5-5 2.5-5z" fill="#fff" transform="rotate(10 12 12)"/>
          </svg>
        </span>
        <span class="contact-item__text">0437259064</span>
      </li>
      <li class="contact-item contact-item--email">
        <span class="contact-icon">
          <svg width="30" height="30" viewBox="0 0 30 30" aria-hidden="true" fill="none" stroke="#fff" stroke-width="1.6">
            <circle cx="15" cy="15" r="12"/>
            <ellipse cx="15" cy="15" rx="5" ry="12"/>
            <line x1="3" y1="15" x2="27" y2="15"/>
            <line x1="15" y1="3" x2="15" y2="27"/>
            <line x1="5" y1="9" x2="25" y2="9"/>
            <line x1="5" y1="21" x2="25" y2="21"/>
          </svg>
        </span>
        <span class="contact-item__text">glen@marlowcrest-example.com</span>
      </li>
      <li class="contact-item contact-item--address">
        <span class="contact-icon">
          <svg width="28" height="28" viewBox="0 0 28 28" aria-hidden="true">
            <ellipse cx="14" cy="22" rx="9" ry="3" fill="none" stroke="#aaa" stroke-width="1.4"/>
            <path d="M14 4a5.5 5.5 0 0 0-5.5 5.5C8.5 14 14 21 14 21s5.5-7 5.5-11.5A5.5 5.5 0 0 0 14 4z" fill="#9a9a9a"/>
            <circle cx="14" cy="9.5" r="2" fill="#1c1c1c"/>
          </svg>
        </span>
        <span class="contact-item__text">Name and Address</span>
      </li>
    </ul>
  </section>

  <section class="card-back dark-surface" aria-label="Business card back">
    <div class="card-back__brand brand-mark">
      <div class="brand-mark__circle"></div>
      <div class="brand-mark__name">Marlow Crest Group</div>
    </div>
    <div class="accent-band"><span class="blue"></span><span class="green"></span><span class="orange"></span></div>
    <p class="card-back__details">Glen Varley, Managing Director, 0437259064 and<br>glen@marlowcrest-example.com.au</p>
  </section>

</main>
</body>
</html>
```